Pharmacy handmade, Personalized Medical Cosmetics Label

Medical Cosmetics label, elegant and professional looking. The creams are Dermatologist formulated and are prepared by local Pharmacy. The label should be versatile and allow space for hand writing to be filled by the pharmacist preparing the product.
The following information will be handwritten:
Upper lid - Lid Balm No.5 ; Marigold, Retinol ; 30
Lower Bottom - Teodora Halvik ; Signature ; 01.01.2017
Upper Lid Label
Velluto Skin (logo)
Doctor Series
(circular pattern - Doctor Formulated, Registered Pharmacy, Handmade, Highest Medical Standards)
(Lid Balm No.5 - in hand writing and different color, maybe red)
Key Ingredients: (Marigold, Retinol - in hand writing, same color as above, maybe red)
(box with hand writing 30) ml
Lower Bottom Label (underneath surface of the container)
Made for Velluto Skin by
Pharmacy Lorant, 7 Pelister blvd., Sofia, ph. 0893517460
Patient: (Teodora Halvik- in hand writing)
Pharmacist: (Signature - in hand writing)
Date: (01.01.2017 - in hand writing)
For External Use
good for 60 days after preparation
Ingredients: Retinol, Marigold Extract, Water, Glycerin, Stearyl Alcohol, Wheat Germ Oil, Polysorbate 60, Sesame Oil, Myristyl Myristate, Cetyl Alcohol, Sorbitan Stearate, Phenoxyethanol, Calendula Extract, Cornflower Extract, Sodium Alginate, Sodium Citrate.
The container lid and bottom are 5 cm = 50 mm in diameter. Made from aluminum and contain 30ml or 50ml.
Please refer to the screen shots from my Web Site to get the feeling for the color pallet and professional look. These creams will be sold on this website. They are custom made by a registered Pharmacy right on the spot after the order has been placed. This is why I need more space for the hand written notes made by the pharmacist who prepared the order.
Please make the design professional, simple and serious colors, like light brown, beige, black or dark brown letters, red hand writing (will be filled by pen or thin marker by the Pharmacist by hand, depending on the order, patient name, etc.)
Thank you.
female 24 - 49 year old
Medical

```html
<!DOCTYPE html>
<html lang="en">
<head>
<meta charset="utf-8">
<title>Velluto Skin – Bottom Label</title>
<link rel="stylesheet" href="https://fonts.googleapis.com/css2?family=Poiret+One&display=swap">
<style>
  :root {
    --bg: #ffffff;
    --ring: #a69689;
    --ring-edge: #4d4641;
    --stitch: #8f8680;
    --label-face: #ffffff;
    --text-soft: #bdbab8;
    --text-strong: #2e2b29;
    --rule: #3a3633;
  }
  html, body {
    margin: 0;
    padding: 0;
    width: 1200px;
    height: 1200px;
    overflow: hidden;
    background: var(--bg);
  }
  .label {
    position: relative;
    width: 1200px;
    height: 1200px;
    font-family: "Poiret One", "Century Gothic", sans-serif;
  }
  .label__shape {
    position: absolute;
    inset: 0;
  }
  .label__text {
    position: absolute;
    left: 0;
    width: 1200px;
    text-align: center;
    color: var(--text-soft);
    margin: 0;
  }
  .maker {
    top: 186px;
    font-size: 40px;
    line-height: 52px;
  }
  .usage {
    top: 688px;
    font-size: 31px;
    line-height: 48px;
  }
  .ingredients {
    top: 802px;
    left: 170px;
    width: 860px;
    font-size: 28px;
    line-height: 40px;
  }
  .fill-field {
    position: absolute;
    display: flex;
    align-items: flex-end;
    font-size: 44px;
    color: var(--text-strong);
    line-height: 1;
  }
  .fill-field__name {
    text-align: right;
  }
  .fill-field__line {
    height: 0;
    border-bottom: 2px solid var(--rule);
    margin-bottom: 4px;
    margin-left: 2px;
  }
  .field-patient { top: 392px; left: 248px; }
  .field-patient .fill-field__line { width: 476px; }
  .field-date { top: 482px; left: 296px; }
  .field-date .fill-field__line { width: 476px; }
  .field-pharmacist { top: 572px; left: 172px; }
  .field-pharmacist .fill-field__line { width: 476px; }
</style>
</head>
<body>
<main class="label">
  <svg class="label__shape" width="1200" height="1200" viewBox="0 0 1200 1200" aria-hidden="true">
    <circle cx="600" cy="600" r="588" fill="var(--ring)" stroke="var(--ring-edge)" stroke-width="2"/>
    <circle cx="600" cy="600" r="532" fill="var(--label-face)"/>
    <circle cx="600" cy="600" r="532" fill="none" stroke="var(--stitch)" stroke-width="5" stroke-dasharray="3 5"/>
  </svg>

  <p class="label__text maker">Made for Velluto Skin by<br>Pharmacy Lorant, 7 Pelister blvd.,<br>Sofia, ph. 0893517460</p>

  <div class="fill-field field-patient"><span class="fill-field__name">Patient:</span><span class="fill-field__line"></span></div>
  <div class="fill-field field-date"><span class="fill-field__name">Date:</span><span class="fill-field__line"></span></div>
  <div class="fill-field field-pharmacist"><span class="fill-field__name">Pharmacist:</span><span class="fill-field__line"></span></div>

  <p class="label__text usage">For External Use<br>good for 60 days after preparation</p>

  <p class="label__text ingredients">Ingredients: Retinol, Marigold Extract, Water, Glycerin, Stearyl Alcohol, Wheat Germ Oil, Polysorbate 60, Sesame Oil, Myristyl Myristate, Cetyl Alcohol, Sorbitan Stearate, Phenoxyethanol, Calendula Extract, Cornflower Extract, Sodium Alginate, Sodium Citrate.</p>
</main>
</body>
</html>
```